Bramblewick Craft Studio
Photography and Handmade Jewlrey
Bramblewick Craft Studio - Handmade Crafts
Creative Brief
Use specific fonts
Try both standard and logo fonts
Bright & Fun-filled
Gordon Pellaway
Owner
PO Box 583 Canyonville, OR 97418
Gordy@bramblewickcraftstudio.com
www.bramblewickcraftstudio.com
We want some thing that is creative that reminds you of our business and fits with the logo
Our ideas are just the logo, and/or the things we offer. But be creative! We're looking for ideas..

```html
<!DOCTYPE html>
<html lang="en">
<head>
<meta charset="utf-8">
<title>Bramblewick Craft Studio – Business Card</title>
<link rel="stylesheet" href="https://fonts.googleapis.com/css2?family=Open+Sans:wght@400;600;700&display=swap">
<style>
  :root {
    --page: #eeeeee;
    --card: #fbfbfb;
    --ink: #333333;
    --ink-soft: #555555;
    --rule: #9a9a9a;
    --sky: #1f8fd6;
    --sky-light: #6cc4ee;
    --night: #1d1d1f;
    --sun: #f29a1f;
  }
  * { box-sizing: border-box; margin: 0; padding: 0; }
  html, body { width: 1200px; height: 471px; overflow: hidden; }
  body {
    background: var(--page);
    font-family: "Open Sans", Arial, sans-serif;
    color: var(--ink);
    position: relative;
  }
  .card {
    position: absolute;
    top: 72px;
    width: 507px;
    height: 293px;
    background: var(--card);
    border-radius: 16px;
    box-shadow: 0 3px 10px rgba(0,0,0,.18);
    overflow: hidden;
  }
  .card--front { left: 62px; }
  .card--back { left: 614px; }

  .brand__dot {
    position: absolute;
    left: 40px;
    top: 28px;
    width: 130px; height: 130px;
    border-radius: 50%;
    background: var(--sky);
  }
  .brand__name {
    position: absolute;
    left: 200px;
    top: 56px;
    width: 290px;
    font-size: 26px;
    font-weight: 600;
    color: var(--sky);
    line-height: 1.15;
  }

  .person {
    position: absolute;
    right: 319px;
    top: 164px;
    text-align: right;
    white-space: nowrap;
  }
  .person__name { font-size: 16px; font-weight: 700; color: var(--ink); }
  .person__role { font-size: 13px; color: var(--ink-soft); margin-top: 3px; }

  .divider {
    position: absolute;
    left: 209px;
    top: 156px;
    width: 1px;
    height: 80px;
    background: var(--rule);
  }

  .contact {
    position: absolute;
    left: 224px;
    top: 148px;
    list-style: none;
    font-size: 12.5px;
    color: var(--ink-soft);
    white-space: nowrap;
  }
  .contact li {
    height: 23px;
    display: flex;
    align-items: center;
    gap: 8px;
  }
  .contact svg { width: 13px; height: 13px; flex: none; }
  .contact .no-icon { padding-left: 21px; }

  .wave { position: absolute; left: 0; bottom: 0; width: 507px; height: 58px; }

  .back-mark {
    position: absolute;
    inset: 0;
    display: flex;
    flex-direction: column;
    align-items: center;
    justify-content: center;
    gap: 14px;
  }
  .back-mark__dot {
    width: 190px; height: 190px;
    border-radius: 50%;
    background: var(--sky);
  }
  .back-mark__name {
    font-size: 18px;
    font-weight: 600;
    color: var(--sky);
  }
</style>
</head>
<body>
  <section class="card card--front">
    <div class="brand__dot"></div>
    <div class="brand__name">Bramblewick Craft Studio</div>

    <div class="person">
      <div class="person__name">Gordon Pellaway</div>
      <div class="person__role">Owner</div>
    </div>

    <div class="divider"></div>

    <ul class="contact">
      <li class="no-icon">PO Box 583 Marlow Creek, ID 97418</li>
      <li>
        <svg viewBox="0 0 16 16" aria-hidden="true"><path d="M4 1l3 3-2 2c1 2 3 4 5 5l2-2 3 3-2 3C7 15 1 9 1 3z" fill="#333"/></svg>
        (541) 555-0182
      </li>
      <li>
        <svg viewBox="0 0 16 16" aria-hidden="true"><circle cx="8" cy="8" r="7" fill="#555"/><text x="8" y="11.5" font-size="10" text-anchor="middle" fill="#fff" font-family="Arial">@</text></svg>
        Gordy@bramblewickcraftstudio.com
      </li>
      <li>
        <svg viewBox="0 0 16 16" aria-hidden="true"><circle cx="8" cy="8" r="7" fill="#555"/><circle cx="8" cy="8" r="4" fill="none" stroke="#fff" stroke-width="1.2"/><line x1="1" y1="8" x2="15" y2="8" stroke="#fff" stroke-width="1.2"/></svg>
        www.bramblewickcraftstudio.com
      </li>
    </ul>

    <svg class="wave" viewBox="0 0 507 58" preserveAspectRatio="none" aria-hidden="true">
      <path d="M0 6 C150 40 320 36 507 10 L507 58 L0 58 Z" fill="var(--sky-light)"/>
      <path d="M0 18 C160 50 330 46 507 22 L507 58 L0 58 Z" fill="var(--sky)"/>
      <path d="M0 30 C170 58 340 54 507 30 L507 58 L0 58 Z" fill="var(--sun)"/>
      <path d="M0 34 C170 62 340 58 507 34 L507 58 L0 58 Z" fill="var(--night)"/>
    </svg>
  </section>

  <section class="card card--back">
    <div class="back-mark">
      <div class="back-mark__dot"></div>
      <div class="back-mark__name">Bramblewick Craft Studio</div>
    </div>
  </section>
</body>
</html>
```